Design for Magento Sports ecommerce

Looking for a design (the PSD's only) for a web shop selling sports equipment.
We are using Magento but feel free to change any of the standard features/elements in Magento.
We are hoping to see something different and creative. Unlike the usual ecommerce designs from LayoutHarbor etc.

The main categories will be: Running (shoes, clothes etc), football (soccer), Handball, Cycling(equipment only), Fitness, Tennis and Swimming.
Lots of subcategories so easy navigation, like a dropdown, megamenu, might be an obvious choice.

The design should at least include suggestions for: Home Page, Product list, Product view and a CMS page (like About Us).
Updates

Hi everybody

Thanks for all the proposals on the project.
There're some really great ones and I appreciate the time and effort you all put into this.
I'm busy walking through each one and will get back as soon as possible.

Tomas

Target Market(s)

Male & Females between 18-60. anyone doing sports in above categories.

Industry/Entity Type

Fitness

Requirements
Must have
• Filter/Layered Navigation is important. We use Kelvora. See here:
http://www.kelvora-apps.com/demo/seo-layered-navigation-plus/

Manufacturers logo on Product view page.

Related products / Upselling on Product view page.
Nice to have
• Product labels/stickers for marking New products, Special offer etc on Product List and Product View.

Icons instead of text links for Cart, My Account, sorting etc.

Responsive design that can make use of widescreen monitors as well as tablets.

The use of "handwriting" or handwritten icons, like here on pixelforum(sorry), looks awesome. :-)
Should not have
• you can disregard the following Magento features:
Wish list
Email a friend
Reviews

```html
<!DOCTYPE html>
<html lang="en">
<head>
<meta charset="utf-8">
<title>Kinetra – Sports Shop</title>
<link href="https://fonts.googleapis.com/css2?family=Arimo:wght@400;700&family=PT+Sans:wght@400;700&family=Indie+Flower&display=swap" rel="stylesheet">
<style>
:root{
  --blue:#0a73cf;
  --blue-light:#bcd9f2;
  --page:#dcdcdc;
  --ink:#2b2b2b;
  --muted:#555;
  --band:#a8a8a8;
  --footer:#2a2a2a;
  --white:#fff;
}
*{margin:0;padding:0;box-sizing:border-box}
html,body{width:757px;height:1200px;overflow:hidden}
body{position:relative;background:var(--page);font-family:"Arimo",Arial,sans-serif;color:var(--ink)}
.abs{position:absolute}
.topbar{left:0;top:0;width:757px;height:83px;background:var(--blue)}
.util-icons{left:204px;top:7px;display:flex;gap:8px}
.top-links{left:513px;top:27px;font:7px "PT Sans",sans-serif;color:#dbe9f7;letter-spacing:.2px}
.cart-note{left:513px;top:44px;font:7px "PT Sans",sans-serif;color:#dbe9f7}
.cart-note b{color:#fff}
.search{left:513px;top:62px;width:121px;height:13px;background:#fff;font:7px "PT Sans",sans-serif;color:var(--blue);text-align:right;padding:3px 5px 0 0}
.hero{left:0;top:83px;width:757px;height:266px;background:linear-gradient(100deg,#cfcfcf 0%,#a8a8a8 45%,#8b8f94 62%,#c9c9c9 100%)}
.brand{left:119px;top:29px;width:136px;height:54px;background:#fff;border-radius:34px 0 0 0;text-align:center;padding-top:11px}
.brand-name{font:700 21px "PT Sans",sans-serif;color:#111;display:inline-flex;align-items:center;gap:4px}
.brand-name i{display:inline-block;width:12px;height:12px;background:var(--blue)}
.brand-url{font:700 5px "PT Sans",sans-serif;color:var(--blue);margin-top:1px}
.cat-menu{left:119px;top:83px;width:136px;height:154px;background:var(--blue);border-radius:0 0 46px 0;list-style:none;padding-top:20px}
.cat-menu li{font:400 8.5px "PT Sans",sans-serif;color:#fff;padding-left:41px;height:20.3px}
.subnav{left:136px;top:88px;width:319px;height:19px;background:#e4e4e4;border-radius:0 10px 10px 0;display:flex;align-items:center;font:700 7.5px "PT Sans",sans-serif;color:#222}
.subnav .current{width:119px;height:19px;background:var(--blue-light);border-radius:10px 0 0 10px;color:var(--blue);padding:5px 0 0 24px;font-weight:400;font-size:8.5px}
.subnav span.sep{margin:0 7px}
.subnav .first{margin-left:20px}
.section-title{font:400 16px "Indie Flower",cursive;color:#333;display:flex;align-items:center}
.section-title::after{content:"";flex:1;border-bottom:1px dotted #555;margin-left:5px;margin-top:4px}
.welcome-title{left:118px;top:366px;width:516px}
.intro{left:118px;top:404px;width:516px;font-size:7.3px;line-height:8.6px;color:#333;text-align:justify}
.intro p{margin-bottom:8px}
.featured-title{left:118px;top:495px;width:516px}
.tile{width:136px;height:124px;background:#fff;border-radius:0 38px 0 38px}
.tile-img{position:absolute;left:28px;top:18px;width:80px;height:88px;border-radius:10px}
.tile--active{border:3px solid #bdbdbd}
.tile-label{position:absolute;left:0;right:0;top:47px;height:28px;background:rgba(160,160,160,.75);color:#fff;font:700 8px "PT Sans",sans-serif;text-align:center;line-height:28px}
.col-title{font:400 15px "Indie Flower",cursive;color:#333}
.bestsellers{left:118px;top:835px;width:137px}
.bestsellers ol{list-style:none;margin-top:12px}
.bestsellers li{font-size:7.3px;color:#333;height:27.8px;padding-top:6px;border-bottom:1px dotted #888;padding-left:1px}
.divider{top:843px;width:1px;height:170px;background:#bdbdbd}
.offers{left:306px;top:835px;width:137px}
.offer-tag{position:absolute;left:0;top:34px;font:700 25px "PT Sans",sans-serif;color:#333;line-height:24px}
.offer-tag small{display:block;font-size:10px;line-height:11px}
.offer-img{position:absolute;left:56px;top:36px;width:83px;height:56px;border-radius:6px;background:linear-gradient(135deg,#2a2d35,#1d5fb8 70%,#cfd6e0)}
.col-text{font-size:7.3px;line-height:8.4px;color:#333;text-align:justify}
.offers .col-text{position:absolute;top:112px;width:137px}
.btn{position:absolute;width:50px;height:15px;background:var(--blue);color:#fff;font:400 7.5px "Arimo",sans-serif;text-align:center;line-height:15px;border-radius:1px}
.connected{left:498px;top:835px;width:136px}
.email{position:absolute;top:75px;width:136px;height:12px;background:#f1f1f1;font:italic 6.5px "Arimo",sans-serif;color:#777;text-align:center;line-height:12px}
.connected .col-text{position:absolute;top:95px;width:136px}
.payband{left:0;top:1031px;width:757px;height:46px;background:var(--band)}
.pay-title{left:118px;top:1042px;font:400 15px "Indie Flower",cursive;color:#333}
.cards{left:277px;top:1045px;display:flex;gap:18.5px}
.card{width:29px;height:18px;background:#f2f2f2;border-radius:2px;font:700 5.5px "Arimo",sans-serif;color:#1c3f8a;text-align:center;line-height:18px}
.footer{left:0;top:1077px;width:757px;height:123px;background:var(--footer);color:#cfcfcf}
.fcol{position:absolute;top:17px}
.fcol h4{font:400 8px "Arimo",sans-serif;color:#fff;margin-bottom:4px}
.fcol li{list-style:none;font-size:6.8px;line-height:10.2px;color:#bbb}
.copyright{position:absolute;left:0;right:0;top:106px;text-align:center;font-size:6.5px;color:#ccc}
</style>
</head>
<body>
<header>
  <div class="abs topbar"></div>
  <div class="abs util-icons" aria-label="Account, cart and delivery">
    <svg width="10" height="10" viewBox="0 0 10 10"><circle cx="5" cy="3" r="2.4" fill="#fff"/><path d="M0.5 10 Q5 4.5 9.5 10Z" fill="#fff"/></svg>
    <svg width="12" height="10" viewBox="0 0 12 10"><path d="M0 1h2l2 6h6l1.5-4.5H3" stroke="#fff" stroke-width="1.3" fill="none"/><circle cx="5" cy="9" r="1" fill="#fff"/><circle cx="9" cy="9" r="1" fill="#fff"/></svg>
    <svg width="13" height="10" viewBox="0 0 13 10"><rect x="0" y="2" width="8" height="5" fill="#fff"/><path d="M8 3.5h3l2 2V7H8z" fill="#fff"/><circle cx="3" cy="8.5" r="1.2" fill="#fff"/><circle cx="10.5" cy="8.5" r="1.2" fill="#fff"/></svg>
  </div>
  <div class="abs top-links">SHOP ONLINE &nbsp;|&nbsp; SIGN UP &nbsp;|&nbsp; LOGIN</div>
  <div class="abs cart-note">YOUR SHOPPING CART HAS <b>(0)</b> ITEAM</div>
  <div class="abs search">SEARCH</div>
</header>

<div class="abs hero" role="img" aria-label="Photo of a sprinter in a blue running suit bursting forward from the start"></div>

<div class="abs brand">
  <div class="brand-name">Kinetra<i></i></div>
  <div class="brand-url">www.kinetra-shop.dk</div>
</div>

<nav>
  <ul class="abs cat-menu">
    <li></li><li>FOOTBALL</li><li>HANDBALL</li><li>CYCLING</li><li>FITNESS</li><li>TENNIS</li><li>SWIMMING</li>
  </ul>
  <div class="abs subnav">
    <span class="current">RUNNING</span>
    <span class="first">SHOES</span><span class="sep">|</span><span>CLOTHS</span><span class="sep">|</span><span>TIMERS</span><span class="sep">|</span><span>MEDI</span>
  </div>
</nav>

<main>
  <h2 class="abs section-title welcome-title">Welcome to Kinetra</h2>
  <div class="abs intro">
    <p>Lorem ipsum dolor sit amet, consectetuer adipiscing elit. Aenean commodo ligula eget dolor. Aenean massa. Cum sociis natoque penatibus et magnis dis parturient montes, nascetur ridiculus mus. Donec quam felis, ultricies nec, pellentesque eu, pretium quis, sem. Nulla consequat massa quis enim.</p>
    <p>Donec pede justo, fringilla vel, aliquet nec, vulputate eget, arcu. In enim justo, rhoncus ut, imperdiet a, venenatis vitae, justo. Nullam dictum felis eu pede mollis pretium. Integer tincidunt. Lorem ipsum dolor sit amet, consectetuer adipiscing elit. Aenean commodo ligula eget dolor. Aenean massa. Cum sociis natoque penatibus et magnis dis parturient montes, nascetur ridiculus mus. Donec quam felis, ultricies nec, pellentesque eu, pretium quis, sem. Nulla consequat massa quis enim.</p>
  </div>

  <h2 class="abs section-title featured-title">Featured Products</h2>
  <div class="abs tile tile--active" style="left:119px;top:535px">
    <div class="tile-img" role="img" aria-label="Green and white running shoe" style="background:linear-gradient(135deg,#8cc63f,#d9d9d9)"></div>
    <div class="tile-label">SHOES</div>
  </div>
  <div class="abs tile" style="left:308px;top:535px"><div class="tile-img" role="img" aria-label="Black sports t-shirt" style="background:#1b1b1b"></div></div>
  <div class="abs tile" style="left:498px;top:535px"><div class="tile-img" role="img" aria-label="Treadmill" style="background:linear-gradient(160deg,#6b6b6b,#c4c4c4)"></div></div>
  <div class="abs tile" style="left:119px;top:681px"><div class="tile-img" role="img" aria-label="Black and white football" style="background:radial-gradient(circle,#f0f0f0 30%,#333 90%);border-radius:50%"></div></div>
  <div class="abs tile" style="left:308px;top:681px"><div class="tile-img" role="img" aria-label="Yellow sports watch" style="background:linear-gradient(135deg,#f5e21b,#d6c30c)"></div></div>
  <div class="abs tile" style="left:498px;top:681px"><div class="tile-img" role="img" aria-label="Blue tennis racket" style="background:linear-gradient(135deg,#d4d4d4,#2f6fd4)"></div></div>

  <section class="abs bestsellers">
    <h3 class="col-title">Best sellers</h3>
    <ol>
      <li>1. Suspendisse nec nunc et pik snisi</li>
      <li>2. DDdce et nulla sed neque placerat</li>
      <li>3. Aliquam sollicitudin lacus egesadt</li>
      <li>4. Suspendisse nec nunc et pik snisi</li>
      <li>5. Pulputate Proin sollicitudin turpis</li>
    </ol>
  </section>
  <div class="abs divider" style="left:282px"></div>

  <section class="abs offers">
    <h3 class="col-title">Latest Offers</h3>
    <div class="offer-tag">30%<small>SPECIAL<br>DISCOUNT</small></div>
    <div class="offer-img" role="img" aria-label="Black and blue high-top sneaker"></div>
    <p class="col-text">ricies nec, pellentesque eu, pretium quis, sem. Nulla consequat massa quis enim.</p>
    <div class="btn" style="left:88px;top:150px">Get It</div>
  </section>
  <div class="abs divider" style="left:475px"></div>

  <section class="abs connected">
    <h3 class="col-title">Stay Connected</h3>
    <svg style="position:absolute;left:52px;top:30px" width="32" height="30" viewBox="0 0 32 30" aria-label="Newsletter"><rect x="1" y="6" width="30" height="22" fill="#e9edf2" stroke="#c4ccd6"/><path d="M1 6 L16 18 L31 6" fill="#6aaee8" stroke="#3d8bd6"/><rect x="7" y="1" width="18" height="10" fill="#fff" stroke="#c4ccd6"/></svg>
    <div class="email">Enter your email id</div>
    <p class="col-text">ricies nec, pellentesque eu, pretium quis, sem.Nulla consequat massauis enim.ricies nec, pellentesqu,pretium quis, sem. Nulla consequat massa quis enim.</p>
    <div class="btn" style="left:86px;top:150px">Subscribe</div>
  </section>
</main>

<div class="abs payband"></div>
<div class="abs pay-title">Trusted payment options</div>
<div class="abs cards">
  <div class="card">Paylo</div><div class="card">Cardix</div><div class="card">Amerpay</div><div class="card">BANK</div>
  <div class="card">Paylo</div><div class="card">Cardix</div><div class="card">Amerpay</div><div class="card">BANK</div>
</div>

<footer class="abs footer">
  <div class="fcol" style="left:118px"><h4>CUSTOMER SERVICES</h4><ul><li>Running</li><li>Football</li><li>handball</li><li>Fitness</li><li>Tennis</li><li>Swimming</li></ul></div>
  <div class="fcol" style="left:249px"><h4>QUICK LINKS</h4><ul><li>Running</li><li>Football</li><li>handball</li><li>Fitness</li><li>Tennis</li><li>Swimming</li></ul></div>
  <div class="fcol" style="left:347px"><h4>CUSTOMER ACCOUNT</h4><ul><li>Running</li><li>Football</li><li>handball</li><li>Fitness</li><li>Tennis</li><li>Swimming</li></ul></div>
  <div class="fcol" style="left:480px"><h4>CUSTOMER SUPPORT</h4><ul><li>Running</li><li>Football</li><li>handball</li><li>Fitness</li><li>Tennis</li><li>Swimming</li></ul></div>
  <div class="fcol" style="left:608px"><h4>CARRERS</h4><ul><li>Running</li><li>Football</li><li>handball</li><li>Fitness</li><li>Tennis</li><li>Swimming</li></ul></div>
  <div class="copyright">Copyright © 2013 Kinetra ®. All Rights Reserved.</div>
</footer>
</body>
</html>
```